KESTREL REFRIGERATION Business Card design

We are looking for a business card design front and back. We would like our logo only on the front with all other details on the rear.
Rear should include name, email address and two phone numbers. Similar to the attachment.
Smart and bright.
Looking for a matt finish on all of the card but the logo to be gloss and slightly proud.

Contact Information for Business Card

Name - Gavin Holloway
Director
Phone - 0867302948
0417259083
email - gavin@kestrelrefrigeration.com.au
website - kestrelrefrigeration.com.au

Font styles to use
Serif

Requirements
Must have
• Colours from our logo. icons for phone, email etc.

```html
<!DOCTYPE html>
<html lang="en">
<head>
<meta charset="utf-8">
<title>Kestrel Refrigeration Business Card</title>
<link rel="stylesheet" href="https://fonts.googleapis.com/css2?family=Roboto+Slab:wght@400;700&display=swap">
<style>
  :root {
    --purple: #452a6b;
    --lime: #add066;
    --white: #ffffff;
    --ink: #3a3346;
    --muted: #6d6878;
    --backdrop: #232323;
  }
  * { box-sizing: border-box; margin: 0; padding: 0; }
  html, body {
    width: 1200px; height: 856px; overflow: hidden;
    background: var(--backdrop);
    font-family: "Roboto Slab", Georgia, serif;
  }
  .canvas { position: relative; width: 1200px; height: 856px; }

  .card {
    position: absolute;
    width: 560px; height: 320px;
    box-shadow: 0 14px 30px rgba(0,0,0,.55);
    overflow: hidden;
  }

  /* Front */
  .card-front { left: 60px; top: 70px; background: var(--purple); }
  .wordmark {
    color: var(--lime);
    font-weight: 700;
    text-align: center;
    line-height: 1;
  }
  .card-front .wordmark { position: absolute; left: 0; right: 0; top: 92px; }
  .wordmark-main { display: block; font-size: 64px; letter-spacing: 1px; }
  .wordmark-sub { display: block; font-size: 20px; letter-spacing: 3px; margin-top: 8px; }
  .front-url {
    position: absolute; left: 0; right: 0; bottom: 44px;
    text-align: center; color: var(--white);
    font-size: 14px; letter-spacing: 1.5px;
  }
  .front-url .domain { color: var(--lime); }

  /* Back */
  .card-back { left: 580px; top: 466px; background: var(--white); }
  .card-back .wordmark { position: absolute; left: 22px; top: 128px; width: 250px; }
  .card-back .wordmark-main { font-size: 44px; }
  .card-back .wordmark-sub { font-size: 14px; letter-spacing: 2px; }

  .details { position: absolute; left: 300px; top: 42px; width: 250px; }
  .block { position: relative; padding-left: 14px; margin-bottom: 14px; }
  .block::before {
    content: ""; position: absolute; left: 0; top: 2px; bottom: 2px;
    width: 2px; background: var(--purple);
  }
  .block-contact::before { background: var(--lime); }
  .person-name { color: var(--lime); font-weight: 700; font-size: 20px; letter-spacing: .5px; }
  .person-role { color: var(--muted); font-size: 12px; }
  .address { color: var(--ink); font-size: 12px; line-height: 1.35; }
  .contact-list { list-style: none; }
  .contact-item {
    display: flex; align-items: center; gap: 7px;
    color: var(--ink); font-size: 11.5px; line-height: 1.55;
    white-space: nowrap;
  }
  .contact-item svg { width: 11px; height: 11px; flex: none; fill: var(--purple); }

  .band-lime {
    position: absolute; left: 0; bottom: 0;
    width: 68%; height: 20px; background: var(--lime);
  }
  .band-purple {
    position: absolute; right: 0; bottom: 0;
    width: 32%; height: 44px; background: var(--purple);
  }
</style>
</head>
<body>
<main class="canvas">

  <section class="card card-front" aria-label="Card front">
    <div class="wordmark">
      <span class="wordmark-main">KESTREL</span>
      <span class="wordmark-sub">REFRIGERATION</span>
    </div>
    <p class="front-url">www.<span class="domain">kestrelrefrigeration</span>.com.au</p>
  </section>

  <section class="card card-back" aria-label="Card back">
    <div class="wordmark">
      <span class="wordmark-main">KESTREL</span>
      <span class="wordmark-sub">REFRIGERATION</span>
    </div>

    <div class="details">
      <div class="block">
        <p class="person-name">GAVIN HOLLOWAY</p>
        <p class="person-role">Director</p>
      </div>
      <div class="block">
        <p class="address">Your Address here<br>Suite 214, Westvale 60210</p>
      </div>
      <div class="block block-contact">
        <ul class="contact-list">
          <li class="contact-item">
            <svg viewBox="0 0 12 12" aria-hidden="true"><path d="M3 0h6a1 1 0 0 1 1 1v10a1 1 0 0 1-1 1H3a1 1 0 0 1-1-1V1a1 1 0 0 1 1-1zm0 1.5v7.5h6V1.5z"/></svg>
            0867302948
          </li>
          <li class="contact-item">
            <svg viewBox="0 0 12 12" aria-hidden="true"><path d="M2.5 0.5l2 2.3-1.1 1.4c.7 1.6 2 2.9 3.6 3.6l1.4-1.1 2.3 2-1.4 2.3C4.6 10.6 1.4 7.4.2 2.7z"/></svg>
            0417259083
          </li>
          <li class="contact-item">
            <svg viewBox="0 0 12 12" aria-hidden="true"><path d="M0 2h12v1L6 7 0 3zm0 2.3l6 4 6-4V10H0z"/></svg>
            gavin@kestrelrefrigeration.com.au
          </li>
          <li class="contact-item">
            <svg viewBox="0 0 12 12" aria-hidden="true"><circle cx="6" cy="6" r="5.5"/><path d="M.5 6h11M6 .5v11M2 3h8M2 9h8" stroke="#fff" stroke-width=".8" fill="none"/></svg>
            kestrelrefrigeration.com.au
          </li>
        </ul>
      </div>
    </div>

    <div class="band-lime"></div>
    <div class="band-purple"></div>
  </section>

</main>
</body>
</html>
```